Flooring & Interior Design showroom

Just bought this business- Kestrel Lane Flooring & Interiors. Love our logo (we are on Kestrel Lane )and colors
Forest green, gold and black
Love that the back lists everything we do. We no longer have plenotilex but need to add in LVP/ SPC and need to take out vantor shadehub logo at the bottom and use the quib logo instead (maybe? open to suggestions)

Not in love with our cards- I want a higher end look
I hate the gradient poop color we have now.
Would love if they were all black - maybe or ??
or had a foil or embossing?

```html
<!DOCTYPE html>
<html lang="en">
<head>
<meta charset="utf-8">
<title>Kestrel Lane Flooring &amp; Interiors — Business Cards</title>
<link rel="stylesheet" href="https://fonts.googleapis.com/css2?family=Roboto:wght@400;500;700&display=swap">
<style>
  :root {
    --page: #ffffff;
    --ink-dark: #1b1916;
    --ink-dark-2: #25221e;
    --silver-1: #e6e6e6;
    --silver-2: #c9c9c9;
    --gold: #f4e49c;
    --rose: #e7b49a;
    --green: #3e8a4f;
    --green-deep: #1f5a34;
    --border: #c8917a;
    --white: #ffffff;
    --text-dark: #2a2a2a;
  }
  * { margin: 0; padding: 0; box-sizing: border-box; }
  html, body { width: 687px; height: 1200px; overflow: hidden; background: var(--page); }
  body { font-family: "Roboto", sans-serif; position: relative; }

  .card {
    position: absolute; left: 63px; width: 560px; height: 320px;
    overflow: hidden; box-shadow: 0 3px 8px rgba(0,0,0,.25);
  }
  .card--front { top: 250px; background: linear-gradient(180deg, var(--ink-dark-2), var(--ink-dark)); }
  .card--back { top: 630px; background: var(--ink-dark); }

  .brand { position: absolute; display: flex; align-items: center; gap: 10px; }
  .brand__dot { width: 18px; height: 18px; border-radius: 50%; background: var(--green); flex: none; }
  .brand__name { color: var(--green); font-weight: 700; text-transform: uppercase; line-height: 1.15; }
  .brand__name span { display: block; }
  .card--front .brand { left: 0; right: 0; top: 62px; justify-content: center; }
  .card--front .brand__name { font-size: 28px; letter-spacing: 1px; }
  .card--front .brand__name span + span { font-size: 13px; letter-spacing: 2px; }

  .contact { position: absolute; left: 0; right: 0; top: 170px; text-align: center; color: var(--white); }
  .contact__name { font-size: 15px; font-weight: 700; color: var(--gold); }
  .contact__name em { font-style: normal; color: var(--rose); }
  .contact__role { font-size: 13px; color: var(--green); margin-top: 1px; }
  .contact__lines { font-size: 14.5px; margin-top: 5px; }
  .contact__lines b { color: var(--gold); font-weight: 700; margin-right: 4px; }
  .contact__lines .gap { display: inline-block; width: 16px; }
  .contact__address { font-size: 14.5px; margin-top: 6px; display: flex; justify-content: center; align-items: center; gap: 6px; }
  .contact__box {
    display: inline-flex; gap: 16px; margin-top: 9px; padding: 3px 14px;
    border: 1.5px solid var(--border); border-radius: 4px;
    color: var(--green); font-size: 13px;
  }
  .contact__box i { font-style: normal; color: var(--white); }

  .back__top {
    position: absolute; left: 0; top: 0; width: 100%; height: 171px;
    background: linear-gradient(120deg, var(--silver-2), var(--silver-1) 45%, var(--silver-2));
  }
  .tagline { position: absolute; left: 37px; top: 42px; color: var(--text-dark); }
  .tagline__main { font-size: 16.5px; font-weight: 700; }
  .tagline__sub { font-size: 14px; margin-top: 2px; }
  .back__phone { position: absolute; left: 36px; top: 118px; font-size: 19px; color: var(--text-dark); display: flex; align-items: center; gap: 5px; }
  .back__web { position: absolute; left: 36px; top: 143px; font-size: 12.5px; color: var(--green-deep); }
  .card--back .brand { left: 300px; top: 70px; }
  .card--back .brand__name { font-size: 25px; letter-spacing: 1px; color: var(--green-deep); }
  .card--back .brand__name span + span { font-size: 11.5px; letter-spacing: 1.6px; }
  .card--back .brand__dot { background: var(--green-deep); }

  .services { position: absolute; top: 187px; left: 0; width: 100%; height: 90px; list-style: none; color: var(--white); font-size: 12px; }
  .services li { position: absolute; display: flex; align-items: flex-start; gap: 5px; line-height: 1.25; white-space: nowrap; }
  .services .tick { flex: none; width: 8px; height: 8px; margin-top: 3px; }

  .partners { position: absolute; top: 274px; left: 0; width: 100%; color: var(--white); font-size: 14px; font-weight: 700; }
  .partners span { position: absolute; transform: translateX(-50%); display: flex; align-items: center; gap: 5px; }
  .partners .mark { width: 11px; height: 11px; border-radius: 50%; background: var(--white); }
</style>
</head>
<body>

<svg width="0" height="0" style="position:absolute" aria-hidden="true">
  <symbol id="tick" viewBox="0 0 10 10"><circle cx="5" cy="5" r="5" fill="#f4e49c"/><path d="M2.6 5.2l1.6 1.6 3.2-3.4" fill="none" stroke="#1b1916" stroke-width="1.4"/></symbol>
</svg>

<section class="card card--front" aria-label="Business card front">
  <div class="brand">
    <div class="brand__dot"></div>
    <div class="brand__name"><span>Kestrel Lane</span><span>Flooring &amp; Interiors</span></div>
  </div>
  <div class="contact">
    <div class="contact__name">DANA <em>WELLS</em></div>
    <div class="contact__role">Salesperson</div>
    <div class="contact__lines">
      <b>Store</b>555.210.0148<span class="gap"></span><b>Cell</b>555.304.7720<span class="gap"></span><b>Fax</b>555.210.0199
    </div>
    <div class="contact__address">
      <svg width="10" height="14" viewBox="0 0 10 14" aria-hidden="true"><path d="M5 0a5 5 0 0 1 5 5c0 3.5-5 9-5 9S0 8.5 0 5a5 5 0 0 1 5-5z" fill="#3e8a4f"/><circle cx="5" cy="5" r="2" fill="#1b1916"/></svg>
      314 Kestrel Lane, Harbor Point CA 90000
    </div>
    <div class="contact__box"><span>info@kestrelflooring.com</span><i>|</i><span>CA Lic # 482910</span></div>
  </div>
</section>

<section class="card card--back" aria-label="Business card back">
  <div class="back__top"></div>
  <div class="tagline">
    <div class="tagline__main">Home Town Service</div>
    <div class="tagline__sub">Since 1979</div>
  </div>
  <div class="back__phone">
    <svg width="14" height="14" viewBox="0 0 24 24" aria-hidden="true"><path d="M6.6 10.8a15 15 0 0 0 6.6 6.6l2.2-2.2a1 1 0 0 1 1-.25 11.4 11.4 0 0 0 3.6.57 1 1 0 0 1 1 1V20a1 1 0 0 1-1 1A17 17 0 0 1 3 4a1 1 0 0 1 1-1h3.5a1 1 0 0 1 1 1c0 1.25.2 2.45.57 3.57a1 1 0 0 1-.25 1z" fill="#1f5a34"/></svg>
    555.210.0148
  </div>
  <div class="back__web">www.kestrelflooring.com</div>
  <div class="brand">
    <div class="brand__dot"></div>
    <div class="brand__name"><span>Kestrel Lane</span><span>Flooring &amp; Interiors</span></div>
  </div>

  <ul class="services">
    <li style="left:33px;top:0"><svg class="tick"><use href="#tick"/></svg>Area Rugs</li>
    <li style="left:33px;top:19px"><svg class="tick"><use href="#tick"/></svg>Blinds</li>
    <li style="left:33px;top:38px"><svg class="tick"><use href="#tick"/></svg>Carpet</li>

    <li style="left:119px;top:0"><svg class="tick"><use href="#tick"/></svg>Cork</li>
    <li style="left:119px;top:19px"><svg class="tick"><use href="#tick"/></svg>Hardwood</li>
    <li style="left:119px;top:38px"><svg class="tick"><use href="#tick"/></svg>Laminate</li>

    <li style="left:205px;top:0"><svg class="tick"><use href="#tick"/></svg>Sheers</li>
    <li style="left:205px;top:19px"><svg class="tick"><use href="#tick"/></svg>Valances</li>
    <li style="left:205px;top:38px"><svg class="tick"><use href="#tick"/></svg>Vinyl</li>

    <li style="left:283px;top:0"><svg class="tick"><use href="#tick"/></svg>Bed Spreads</li>
    <li style="left:283px;top:19px"><svg class="tick"><use href="#tick"/></svg>Draperies</li>
    <li style="left:283px;top:38px"><svg class="tick"><use href="#tick"/></svg>Fabric</li>

    <li style="left:378px;top:0"><svg class="tick"><use href="#tick"/></svg>Verticals</li>
    <li style="left:378px;top:19px"><svg class="tick"><use href="#tick"/></svg>Pillows</li>
    <li style="left:378px;top:38px"><svg class="tick"><use href="#tick"/></svg>Shutters</li>

    <li style="left:454px;top:0"><svg class="tick"><use href="#tick"/></svg>LVP/ SPC</li>
    <li style="left:454px;top:19px"><svg class="tick"><use href="#tick"/></svg>Upholstery</li>
    <li style="left:454px;top:38px"><svg class="tick"><use href="#tick"/></svg>Motorized<br>Shades</li>
  </ul>

  <div class="partners" aria-label="Partner brands">
    <span style="left:202px">Norvale</span>
    <span style="left:337px">Brightmere<i class="mark"></i></span>
  </div>
</section>

</body>
</html>
```